Fresh new and cool frozen burger box! Come be a part of an amazing project!

Crust Fins and Melts restaurant is expanding into the frozen foods market!
please check out our website to understand the vibe of the company
https://brivanta.ca
this is a line of premium Halal meat, we want to stress our top-notch quality.
we like the orange colours so see what you can do with them. (maybe white and orange combo)
you have lots of creative freedom here, feel free to use the burger photo I am attaching or any image off the website.
logo should be nice and visible.
we want this packaging to really stand out and be special.
Come be a part of an amazing project!
Target Market(s)
Muslim Flails, looking of a quality meat burger. mostly already familiar with our brand
Industry/Entity Type
Frozen food
Look and feel

```html
<!DOCTYPE html>
<html lang="en">
<head>
<meta charset="utf-8">
<title>Brivanta Burger Patties – Box Lid</title>
<link rel="stylesheet" href="https://fonts.googleapis.com/css2?family=Oswald:wght@600;700&family=Montserrat:wght@700&display=swap">
<style>
  :root {
    --stage: #df6337;
    --lid-orange-light: #f29a4e;
    --lid-orange: #e8843f;
    --ink: #2a2526;
    --panel-black: #1d1d1f;
    --white: #fbf7f2;
    --bun-light: #d9a468;
    --bun-deep: #a8683a;
  }
  * { box-sizing: border-box; margin: 0; padding: 0; }
  html, body {
    width: 1200px; height: 840px; overflow: hidden;
    background: var(--stage);
  }
  .canvas {
    position: relative; width: 1200px; height: 840px;
    display: flex; align-items: center; justify-content: center;
  }
  .lid {
    position: relative; width: 1000px; height: 660px;
    display: flex;
    box-shadow: 0 24px 50px rgba(90, 30, 10, 0.35);
  }
  .lid-front {
    position: relative; width: 560px; height: 100%;
    background: linear-gradient(160deg, var(--lid-orange-light), var(--lid-orange));
  }
  .lid-photo-panel {
    position: relative; flex: 1; height: 100%;
    background: var(--panel-black);
    display: flex; align-items: center; justify-content: center;
  }
  .burger-photo {
    width: 380px; height: 480px;
    border-radius: 46% 46% 40% 40% / 40% 40% 32% 32%;
    background: radial-gradient(ellipse at 45% 35%, var(--bun-light), var(--bun-deep) 80%);
  }
  .brand {
    position: absolute; top: 48px; left: 0; right: 0;
    text-align: center; color: var(--white);
  }
  .brand-name {
    display: inline-flex; align-items: center; gap: 12px;
    font-family: "Oswald", sans-serif; font-weight: 700;
    font-size: 46px; line-height: 1.1; letter-spacing: 2px;
  }
  .brand-dot {
    width: 28px; height: 28px; border-radius: 50%;
    background: var(--white);
  }
  .brand-tagline {
    margin-top: 4px;
    font-family: "Montserrat", sans-serif; font-weight: 700; font-size: 16px;
    letter-spacing: 2px; color: var(--ink);
  }
  .product-title {
    position: absolute; top: 160px; left: 0; right: 0;
    text-align: center; line-height: 0.98;
    font-family: "Oswald", sans-serif; font-weight: 700;
    letter-spacing: 3px;
  }
  .title-burger { display: block; font-size: 140px; color: var(--white); }
  .title-patties { display: block; font-size: 140px; color: var(--ink); }
  .piece-count {
    position: absolute; left: 48px; bottom: 52px;
    font-family: "Oswald", sans-serif; color: var(--ink);
    text-align: center; line-height: 1;
  }
  .piece-count .count { display: block; font-size: 52px; font-weight: 700; }
  .piece-count .unit { display: block; font-size: 18px; font-weight: 600; letter-spacing: 1px; }
  .storage-note {
    position: absolute; right: 40px; bottom: 52px;
    font-family: "Oswald", sans-serif; font-weight: 700;
    font-size: 18px; line-height: 1.15; text-align: center;
    color: var(--ink); letter-spacing: 0.5px;
  }
</style>
</head>
<body>
<main class="canvas">
  <section class="lid">
    <div class="lid-front">
      <header class="brand">
        <div class="brand-name"><span class="brand-dot"></span>BRIVANTA</div>
        <div class="brand-tagline">Crust • Fins • Melts</div>
      </header>
      <h1 class="product-title">
        <span class="title-burger">BURGER</span>
        <span class="title-patties">PATTIES</span>
      </h1>
      <div class="piece-count"><span class="count">6</span><span class="unit">PIECES</span></div>
      <div class="storage-note">READY-TO-COOK<br>KEEP FROZEN</div>
    </div>
    <div class="lid-photo-panel">
      <div class="burger-photo" role="img" aria-label="Photo of a burger with sesame bun, tomato, cheese, bacon, beef patty and lettuce"></div>
    </div>
  </section>
</main>
</body>
</html>
```